The Pixel Tap Business card.

A Simple card with our Logo and contact information. To give to investors and other professionals.

We are a nerd themed bar.
our target market is young professionals age 21+ but the real purpose of this business card is to present to potential investors and other professionals with our contact information. as we are still looking for funding before we start up.

I am partial to green and my partner likes red we are open to iteration.

Target Market(s)

Investors

Industry/Entity Type

Business

Contact Information for Business Card

Martin Hale (225) 730-6192 kent.h4711@mailnest.test Glen Porter (225) 968-5037 glenp318@mailnest.test

Font styles to use
Serif

Requirements
Nice to have
• Keep it simple but not boring.
• Use the Logos but feel free to edit them to match theme/colors.
• Keep the back clean and use one of the Logos.

```html
<!DOCTYPE html>
<html lang="en">
<head>
<meta charset="utf-8">
<title>The Pixel Tap – Business Card</title>
<link rel="stylesheet" href="https://fonts.googleapis.com/css2?family=Montserrat:wght@800&family=Libre+Baskerville&family=Open+Sans:wght@400&display=swap">
<style>
  :root {
    --bg: #e7e4df;
    --ink: #1b1b1b;
    --paper: #ffffff;
    --red: #e63946;
    --grey: #555555;
    --rule: #d4d4d4;
    --white: #ffffff;
  }
  * { margin: 0; padding: 0; box-sizing: border-box; }
  html, body { width: 1200px; height: 913px; overflow: hidden; }
  body { background: var(--bg); position: relative; }

  .card {
    position: absolute;
    left: 290px;
    width: 620px;
    height: 354px;
    overflow: hidden;
    box-shadow: 0 6px 18px rgba(0,0,0,.18);
  }
  .card--front { top: 60px; background: var(--paper); }
  .card--back  { top: 490px; background: var(--ink); }

  .edge { position: absolute; left: 0; width: 620px; height: 40px; }
  .edge--top { top: 0; }
  .edge--bottom { bottom: 0; }

  .brand-name {
    position: absolute;
    font-family: "Montserrat", sans-serif;
    font-weight: 800;
    text-transform: uppercase;
    letter-spacing: 1px;
    line-height: 1;
  }
  .card--front .brand-name {
    left: 40px; top: 160px; width: 260px;
    font-size: 34px; color: var(--ink); text-align: center;
  }

  .divider {
    position: absolute; left: 330px; top: 95px;
    width: 1px; height: 170px; background: var(--rule);
  }
  .contact { position: absolute; left: 355px; top: 100px; width: 250px; }
  .contact__name {
    font-family: "Libre Baskerville", serif;
    font-size: 19px; color: var(--grey);
    text-transform: uppercase; letter-spacing: .5px;
  }
  .contact__list { list-style: none; margin-top: 72px; }
  .contact__item {
    display: flex; align-items: center; gap: 8px;
    font-family: "Open Sans", sans-serif; font-size: 14px;
    color: var(--grey); line-height: 22px;
  }
  .contact__icon { width: 12px; height: 12px; flex: none; }

  .back-logo {
    position: absolute; left: 0; top: 0; width: 620px; height: 354px;
    display: flex; flex-direction: column; align-items: center; justify-content: center;
  }
  .card--back .brand-name {
    position: static; font-size: 44px; color: var(--white);
  }
  .tagline {
    margin-top: 8px;
    font-family: "Montserrat", sans-serif; font-weight: 800;
    font-size: 13px; letter-spacing: 3px; color: var(--white);
    text-transform: uppercase;
  }
</style>
</head>
<body>

<section class="card card--front" aria-label="Business card front">
  <svg class="edge edge--top" viewBox="0 0 620 40" aria-hidden="true">
    <line x1="0" y1="8" x2="620" y2="8" stroke="var(--ink)" stroke-width="6" stroke-dasharray="110 14 40 14"/>
    <line x1="0" y1="17" x2="620" y2="17" stroke="var(--red)" stroke-width="4" stroke-dasharray="150 14 60 14"/>
  </svg>

  <div class="brand-name">The Pixel Tap</div>

  <div class="divider"></div>

  <div class="contact">
    <p class="contact__name">Glen Porter</p>
    <ul class="contact__list">
      <li class="contact__item">
        <svg class="contact__icon" viewBox="0 0 24 24" aria-hidden="true"><path fill="var(--red)" d="M6.6 10.8a15.1 15.1 0 0 0 6.6 6.6l2.2-2.2a1 1 0 0 1 1-.25 11.4 11.4 0 0 0 3.6.57 1 1 0 0 1 1 1V20a1 1 0 0 1-1 1A17 17 0 0 1 3 4a1 1 0 0 1 1-1h3.5a1 1 0 0 1 1 1c0 1.25.2 2.45.57 3.57a1 1 0 0 1-.25 1z"/></svg>
        (225) 968-5037
      </li>
      <li class="contact__item">
        <svg class="contact__icon" viewBox="0 0 24 24" aria-hidden="true"><rect x="2" y="5" width="20" height="14" fill="none" stroke="var(--red)" stroke-width="2.5"/><path d="M2 6l10 7 10-7" fill="none" stroke="var(--red)" stroke-width="2.5"/></svg>
        glenp318@mailnest.test
      </li>
    </ul>
  </div>

  <svg class="edge edge--bottom" viewBox="0 0 620 40" aria-hidden="true">
    <line x1="0" y1="23" x2="620" y2="23" stroke="var(--red)" stroke-width="4" stroke-dasharray="130 14 50 14"/>
    <line x1="0" y1="32" x2="620" y2="32" stroke="var(--ink)" stroke-width="6" stroke-dasharray="90 14 70 14"/>
  </svg>
</section>

<section class="card card--back" aria-label="Business card back">
  <svg class="edge edge--top" viewBox="0 0 620 40" aria-hidden="true">
    <line x1="0" y1="8" x2="620" y2="8" stroke="var(--white)" stroke-width="4" stroke-dasharray="140 14 50 14"/>
    <line x1="0" y1="16" x2="620" y2="16" stroke="var(--red)" stroke-width="5" stroke-dasharray="110 14 70 14"/>
  </svg>

  <div class="back-logo">
    <div class="brand-name">The Pixel Tap</div>
    <div class="tagline">Lounge and Arcade</div>
  </div>

  <svg class="edge edge--bottom" viewBox="0 0 620 40" aria-hidden="true">
    <line x1="0" y1="24" x2="620" y2="24" stroke="var(--red)" stroke-width="5" stroke-dasharray="120 14 60 14"/>
    <line x1="0" y1="32" x2="620" y2="32" stroke="var(--white)" stroke-width="4" stroke-dasharray="150 14 40 14"/>
  </svg>
</section>

</body>
</html>
```